professional business card

A Clean looking business card for a money transfer company. Our company is call Velorix= Transfer + Send = Transcend (next level)
to show professionalism as well as some effects to show digital tech.

1 side to have position, name and address
2 side to have company name and show that we provide money exchange and cross-border money transfer

Target Market(s)

Remittance companies and high net worth individuals

Industry/Entity Type

Finance

Contact Information for Business Card

Name, address, email, title, services- money exchange and cross-border remittance

Requirements
Nice to have
• Digital age feel

```html
<!DOCTYPE html>
<html lang="en">
<head>
<meta charset="utf-8">
<title>Velorix – Business Card</title>
<link rel="stylesheet" href="https://fonts.googleapis.com/css2?family=Montserrat:wght@600&family=Roboto:wght@400;500&display=swap">
<style>
  :root {
    --backdrop: #222222;
    --card: #0c1131;
    --accent: #4ccbf3;
    --ink: #ffffff;
    --map-tone: #18224a;
    --tag-band: rgba(255, 255, 255, 0.08);
  }
  * { margin: 0; padding: 0; box-sizing: border-box; }
  html, body {
    width: 1200px;
    height: 1000px;
    overflow: hidden;
    background: var(--backdrop);
    font-family: "Roboto", Arial, sans-serif;
  }
  .card {
    position: absolute;
    left: 319px;
    width: 561px;
    height: 322px;
    background: var(--card);
    overflow: hidden;
  }
  .card--front { top: 138px; }
  .card--back { top: 540px; }

  .pixel-field {
    position: absolute;
    background: linear-gradient(135deg, var(--accent) 0%, rgba(76, 203, 243, 0.55) 55%, rgba(76, 203, 243, 0) 100%);
    opacity: 0.85;
  }
  .pixel-field--front { left: 8px; top: 10px; width: 156px; height: 124px; }
  .pixel-field--back {
    left: 384px; top: 172px; width: 154px; height: 123px;
    background: linear-gradient(315deg, var(--accent) 0%, rgba(76, 203, 243, 0.55) 55%, rgba(76, 203, 243, 0) 100%);
  }

  .world-map {
    position: absolute;
    left: 64px; top: 68px;
    width: 408px; height: 205px;
    background: radial-gradient(ellipse at center, var(--map-tone) 0%, rgba(24, 34, 74, 0.6) 60%, rgba(24, 34, 74, 0) 100%);
  }

  .brand {
    position: absolute;
    left: 105px; top: 92px;
    display: flex;
    align-items: center;
    gap: 22px;
  }
  .brand__mark {
    width: 56px; height: 56px;
    background: var(--accent);
  }
  .brand__name {
    font-family: "Montserrat", Arial, sans-serif;
    font-weight: 600;
    font-size: 56px;
    line-height: 1;
    color: var(--ink);
    letter-spacing: -0.5px;
    text-transform: uppercase;
  }

  .services {
    position: absolute;
    left: 115px; top: 204px;
    width: 332px; height: 60px;
    background: var(--tag-band);
    display: flex;
    flex-direction: column;
    justify-content: center;
    align-items: center;
    color: var(--ink);
    font-weight: 500;
    font-size: 15px;
    line-height: 22px;
    letter-spacing: 4px;
    text-transform: uppercase;
    text-align: center;
  }

  .person {
    position: absolute;
    left: 76px; top: 80px;
    color: var(--accent);
    text-transform: uppercase;
  }
  .person__name {
    font-weight: 500;
    font-size: 32px;
    letter-spacing: 1.5px;
    line-height: 36px;
  }
  .person__title {
    font-weight: 400;
    font-size: 22px;
    letter-spacing: 1.5px;
    line-height: 26px;
  }

  .contacts {
    position: absolute;
    left: 55px; top: 159px;
    list-style: none;
    color: var(--ink);
    font-size: 14px;
    letter-spacing: 0.8px;
  }
  .contacts__item {
    display: flex;
    align-items: center;
    gap: 6px;
    height: 26px;
    text-transform: uppercase;
  }
  .contacts__icon { width: 18px; height: 18px; flex: none; }
</style>
</head>
<body>

<section class="card card--front">
  <div class="pixel-field pixel-field--front" role="img" aria-label="Grid of small cyan squares fading into the card"></div>
  <div class="world-map" role="img" aria-label="Faint world map in the background"></div>
  <div class="brand">
    <span class="brand__mark"></span>
    <span class="brand__name">Velorix</span>
  </div>
  <p class="services">
    <span>Money exchange and</span>
    <span>Cross-border remittance</span>
  </p>
</section>

<section class="card card--back">
  <div class="person">
    <h1 class="person__name">Daren Holt</h1>
    <p class="person__title">Manager</p>
  </div>
  <ul class="contacts">
    <li class="contacts__item">
      <svg class="contacts__icon" viewBox="0 0 20 20" aria-hidden="true">
        <circle cx="10" cy="10" r="9" fill="none" stroke="#4ccbf3" stroke-width="1.2"/>
        <path d="M10 4.5a3.6 3.6 0 0 0-3.6 3.6c0 2.7 3.6 6.6 3.6 6.6s3.6-3.9 3.6-6.6A3.6 3.6 0 0 0 10 4.5z" fill="#4ccbf3"/>
        <circle cx="10" cy="8.1" r="1.3" fill="#0c1131"/>
      </svg>
      <span>Your street address here</span>
    </li>
    <li class="contacts__item">
      <svg class="contacts__icon" viewBox="0 0 20 20" aria-hidden="true">
        <circle cx="10" cy="10" r="9" fill="none" stroke="#4ccbf3" stroke-width="1.2"/>
        <rect x="5" y="6.5" width="10" height="7" rx="1" fill="#4ccbf3"/>
        <path d="M5.3 7l4.7 3.6L14.7 7" fill="none" stroke="#0c1131" stroke-width="1"/>
      </svg>
      <span>yourmail@velorix.com</span>
    </li>
    <li class="contacts__item">
      <svg class="contacts__icon" viewBox="0 0 20 20" aria-hidden="true">
        <circle cx="10" cy="10" r="9" fill="none" stroke="#4ccbf3" stroke-width="1.2"/>
        <path d="M6.6 5.2l1.7-.3 1 2.6-1.2.9c.6 1.3 1.6 2.3 2.9 2.9l.9-1.2 2.6 1-.3 1.7c-.1.5-.6.9-1.1.8C9.6 13.3 6.7 10.4 6.4 6.3c0-.5.3-1 .2-1.1z" fill="#4ccbf3"/>
      </svg>
      <span>000 111 222 333</span>
    </li>
  </ul>
  <div class="pixel-field pixel-field--back" role="img" aria-label="Stepped cluster of small cyan squares fading to the left"></div>
</section>

</body>
</html>
```